Indian Wedding Invitation

Hello Designers,

We are looking for a fantastic graphic designer to help us come up with our very own bespoke wedding invitation.

We have a logo which we would like to use (see attached) and a very good idea of the style of invitation we are after.

Specification:

- We would like the wedding invitation to be A5 (landscape) with a pocket within it to allow for 3 inserts.
- The pocket should be at the bottom when you open up the card
- The first insert will be A5, the second will be slightly smaller and then the final one will be slightly smaller than that (so that you can see that there are 3 invites included in the invite) - see attached images for what I am referring to
- We will need all 3 of these to match the design of the card
- Once you open the card, the top of the card will contain some content - like details of where we are getting married / timings / rsvp information etc.
- Content will be provided once we have a view of the design

See attached images for the type of designs we are looking for. Also see: http://www.lorvanpress.co.uk/pocket-fold-invitations.html

We are looking for a fresh approach to this card.

We do not have any preference on colour, but it should work well with the logo design that we have.

Hope this is enough information to get you started. Any questions, please drop me a message or email me on tkelmore@fenwickpost.com. I'm usually very quick at responding.

Thanks!

Industry/Entity Type

Graphic Designer

Requirements
Must have
• Classy and high-end look and feel

Use of subtle colours - nothing bright

```html
<!DOCTYPE html>
<html lang="en">
<head>
<meta charset="utf-8">
<title>Anvi &amp; Devan — Pocket Fold Wedding Invitation</title>
<link rel="stylesheet" href="https://fonts.googleapis.com/css2?family=Cinzel:wght@400;600&display=swap">
<style>
  :root {
    --backdrop: #ececed;
    --card-cream: #ece5c8;
    --card-cream-edge: #ddd3ad;
    --pocket-cream: #e6dcb8;
    --gold: #c3a055;
    --gold-card: #c9a24e;
    --gold-card-edge: #dcbc72;
    --plum-deep: #8a3a5c;
    --plum: #9c4a6e;
    --insert-ivory: #fbf8f1;
    --ink-light: #fbf6ee;
  }
  * { box-sizing: border-box; margin: 0; padding: 0; }
  html, body {
    width: 1200px;
    height: 805px;
    overflow: hidden;
    background: var(--backdrop);
    font-family: "Cinzel", "Trajan Pro", serif;
  }
  .invitation {
    position: absolute;
    left: 40px;
    top: 205px;
    width: 1120px;
    height: 396px;
    display: flex;
  }
  .panel {
    position: relative;
    width: 560px;
    height: 396px;
    background: var(--card-cream);
    border: 1px solid var(--card-cream-edge);
  }
  .panel--cover {
    display: flex;
    align-items: center;
    justify-content: space-between;
    padding: 0 46px;
  }
  .cover-name,
  .monogram {
    color: var(--gold);
    font-size: 32px;
    font-weight: 400;
    letter-spacing: 1px;
  }
  .panel--pocket { overflow: hidden; }
  .pocket-art {
    position: absolute;
    inset: 0;
    width: 560px;
    height: 396px;
  }
  .insert-text { font-family: "Cinzel", serif; fill: var(--ink-light); }
</style>
</head>
<body>
  <main class="invitation">
    <section class="panel panel--cover" aria-label="Inner cover">
      <span class="cover-name">Anvi</span>
      <span class="monogram">A&amp;D</span>
      <span class="cover-name">Devan</span>
    </section>

    <section class="panel panel--pocket" aria-label="Pocket with three inserts">
      <svg class="pocket-art" viewBox="0 0 560 396" xmlns="http://www.w3.org/2000/svg">
        <rect class="insert insert--large" x="20" y="18" width="488" height="340" fill="var(--plum-deep)"/>
        <rect class="insert insert--middle" x="50" y="44" width="440" height="300" fill="var(--insert-ivory)"/>
        <rect class="insert insert--small" x="70" y="68" width="384" height="280" fill="var(--plum)"/>

        <g class="invitation-copy">
          <text class="insert-text" x="190" y="128" text-anchor="middle" font-size="10.5" letter-spacing="0.5">DESERUNT CULPA ENIM EX AUTE</text>
          <text class="insert-text" x="128" y="170" text-anchor="middle" font-size="16">ANVI</text>
          <text class="insert-text" x="192" y="170" text-anchor="middle" font-size="16">A&amp;D</text>
          <text class="insert-text" x="258" y="170" text-anchor="middle" font-size="16">DEVAN</text>
          <text class="insert-text" x="190" y="198" text-anchor="middle" font-size="10">NULLA EST MINIM EIUSMOD</text>
          <text class="insert-text" x="190" y="212" text-anchor="middle" font-size="10">OCCAECAT FUGIAT ESSE SINT</text>
          <text class="insert-text" x="190" y="226" text-anchor="middle" font-size="10">VOLUPTATE. ESSE EU CONSEQ</text>
          <text class="insert-text" x="190" y="240" text-anchor="middle" font-size="10">UT NISI AUTE QUIS.</text>
        </g>

        <g class="reply-card" transform="translate(430 232) rotate(-15)">
          <path d="M0 140 C -40 100 -110 40 -110 -30 C -110 -80 -70 -105 -35 -100 C -15 -97 -4 -85 0 -72 C 4 -85 15 -97 35 -100 C 70 -105 110 -80 110 -30 C 110 40 40 100 0 140 Z"
                fill="var(--gold-card)" stroke="var(--gold-card-edge)" stroke-width="4"/>
          <text class="insert-text" x="0" y="-48" text-anchor="middle" font-size="13">ANVI</text>
          <text class="insert-text" x="0" y="-30" text-anchor="middle" font-size="7">THE FAVOR OF YOUR REPLY</text>
          <text class="insert-text" x="-62" y="-10" font-size="7">NAME</text>
          <line x1="-38" y1="-10" x2="60" y2="-10" stroke="var(--ink-light)" stroke-width="0.6"/>
          <text class="insert-text" x="-62" y="8" font-size="7">AUGUST</text>
          <line x1="-30" y1="8" x2="60" y2="8" stroke="var(--ink-light)" stroke-width="0.6"/>
        </g>

        <path class="pocket" d="M0 226 L14 222 L290 300 L560 246 L560 396 L0 396 Z"
              fill="var(--pocket-cream)" stroke="var(--card-cream-edge)" stroke-width="1.5"/>
      </svg>
    </section>
  </main>
</body>
</html>
```